Upmarket Bathroom and Kitchen ware supplier needs a classy business card design

We are a company based in Fiji, we sell plumbing ware (Kitchen and bathroom taps, Basins,showers, toilets etc) through up market show rooms to individuals and directly through Architects and designers of resorts and holiday houses for new builds and renovations. we are wanting to upgrade our over all look and brand. we are starting with a new logo but will be rebranding the whole business. This project is for a business card design for my management and tales team I would like it to be dark, classy and interesting

Target Market(s)

Resort directors and Management, High end holiday home owners

Contact Information for Business Card

Gavin Threlkeld
Director
+64219473518

Colors

Designer to choose colors to be used in the design.

Requirements
Must have
• Must have an upmarket appearance I like darker charcoal shades but will be guided by the designers
• Please any catch phrases like "Crafting remarkable living rooms" this belongs tpo one of our suppliers so can not be used.
Nice to have
• Double sided, so front dedicated to logo provided and back info about the business and the person.

```html
<!DOCTYPE html>
<html lang="en">
<head>
<meta charset="utf-8">
<title>Coralyn Interiors – Business Card</title>
<link rel="stylesheet" href="https://fonts.googleapis.com/css2?family=Roboto:wght@300&family=Montserrat:wght@300&display=swap">
<style>
  :root {
    --backdrop: #efefef;
    --card-top: #3d3167;
    --card-mid: #2d1f5e;
    --card-bottom: #221453;
    --ink: #ffffff;
    --ink-soft: rgba(255, 255, 255, 0.85);
  }
  * { box-sizing: border-box; margin: 0; padding: 0; }
  html, body {
    width: 1200px;
    height: 1096px;
    overflow: hidden;
    background: var(--backdrop);
  }
  .canvas {
    position: relative;
    width: 1200px;
    height: 1096px;
  }
  .card {
    position: absolute;
    width: 558px;
    height: 362px;
    border-radius: 24px;
    background: linear-gradient(178deg, var(--card-top) 0%, var(--card-top) 18%, var(--card-mid) 55%, var(--card-bottom) 100%);
    color: var(--ink);
    overflow: hidden;
  }
  .card--front { left: 486px; top: 168px; }
  .card--back  { left: 196px; top: 565px; }

  /* Front: brand */
  .brand-dot {
    position: absolute;
    left: 249px;
    top: 100px;
    width: 62px;
    height: 62px;
    border: 2px solid var(--ink);
    border-radius: 50%;
  }
  .brand-name {
    position: absolute;
    left: 0;
    width: 100%;
    top: 220px;
    text-align: center;
    font-family: "Montserrat", sans-serif;
    font-weight: 300;
    font-size: 30px;
    letter-spacing: 17px;
    text-indent: 17px;
    line-height: 1;
  }
  .brand-rule {
    position: absolute;
    left: 180px;
    top: 261px;
    width: 199px;
    height: 1px;
    background: var(--ink-soft);
  }
  .brand-sub {
    position: absolute;
    left: 0;
    width: 100%;
    top: 268px;
    text-align: center;
    font-family: "Montserrat", sans-serif;
    font-weight: 300;
    font-size: 11.5px;
    letter-spacing: 7px;
    text-indent: 7px;
    line-height: 1;
  }

  /* Back: contact */
  .person {
    position: absolute;
    right: 299px;
    top: 152px;
    text-align: right;
    font-family: "Roboto", sans-serif;
    font-weight: 300;
  }
  .person__name {
    font-size: 23px;
    line-height: 1;
    letter-spacing: 0.2px;
    text-transform: uppercase;
  }
  .person__role {
    margin-top: 3px;
    font-size: 13px;
    line-height: 1;
    letter-spacing: 0.5px;
    color: var(--ink-soft);
  }
  .divider {
    position: absolute;
    left: 277px;
    top: 120px;
    width: 3px;
    height: 95px;
    background: var(--ink);
  }
  .phone {
    position: absolute;
    left: 297px;
    top: 152px;
    font-family: "Roboto", sans-serif;
    font-weight: 300;
    font-size: 23px;
    line-height: 1;
    letter-spacing: 0.3px;
  }
</style>
</head>
<body>
  <main class="canvas">
    <section class="card card--front" aria-label="Card front">
      <span class="brand-dot" aria-hidden="true"></span>
      <p class="brand-name">CORALYN</p>
      <span class="brand-rule" aria-hidden="true"></span>
      <p class="brand-sub">INTERIORS</p>
    </section>

    <section class="card card--back" aria-label="Card back">
      <div class="person">
        <p class="person__name">Gavin Threlkeld</p>
        <p class="person__role">DIRECTOR</p>
      </div>
      <span class="divider" aria-hidden="true"></span>
      <p class="phone">+64219473518</p>
    </section>
  </main>
</body>
</html>
```